Energy Company 8-page Brochure

We are in need of a redesign of our 8-page brochure. Attached is the initial design that does not represent us very well. We are looking for CLEAN/CORPORATE look with a little bit of flair (graphs/charts if applicable).

I prefer white background and our company colors (blue/green) to be the accent colors. Feel free to add additional accent colors to highlight certain areas.

We are in the energy field (not just solar), so please consider the types of images that you will use. Are headquarters is located in Chicago, IL so a great looking picture of the skyline or something similar would work for the front and back cover.

We have additional marketing collateral that we will want to be uniformed once we have the right design.

Good luck, and we look forward to receiving some great designs!

Best Regards,
Kurt

Target Market(s)

Small to large businesses (B2B).

Industry/Entity Type

It Company

Colors
ffffff
9bcb3c
0255a3

Requirements
Must have
• Clean design, company colors, specified content and editable files.
Nice to have
• Graphs, charts, highlighted areas where necessary.
Should not have
• Clutter! Please utilized page space appropriately. There is a lot of content, so you need to consider graphics and image placement.

```html
<!DOCTYPE html>
<html lang="en">
<head>
<meta charset="utf-8">
<title>Lakeshore Power – Brochure Covers</title>
<link rel="stylesheet" href="https://fonts.googleapis.com/css2?family=Open+Sans:wght@300;400;600;700&display=swap">
<style>
  :root {
    --brand-blue: #0255a3;
    --brand-green: #5a9a2e;
    --brand-green-light: #9bcb3c;
    --paper: #ffffff;
    --paper-shade: #f1f1f1;
    --backdrop: #d9d9d9;
    --ink-grey: #6d6d6d;
  }
  * { box-sizing: border-box; margin: 0; padding: 0; }
  html, body {
    width: 1200px; height: 800px; overflow: hidden;
    background: var(--backdrop);
    font-family: "Open Sans", Arial, sans-serif;
  }
  .spread {
    position: absolute; left: 120px; top: 90px;
    width: 960px; height: 620px;
    display: flex;
    box-shadow: 0 6px 22px rgba(0,0,0,0.18);
  }
  .page {
    position: relative; width: 480px; height: 620px;
    background: var(--paper);
  }
  .page--front { background: linear-gradient(90deg, var(--paper-shade) 0%, var(--paper) 12%); }

  /* Brand lockups */
  .lockup { position: absolute; display: flex; flex-direction: column; gap: 18px; }
  .brand { display: flex; align-items: center; gap: 8px; color: var(--brand-blue); font-weight: 400; font-size: 17px; line-height: 1.1; }
  .brand--efficiency { color: var(--brand-green); }
  .brand__dot { width: 26px; height: 26px; border-radius: 50%; background: var(--brand-blue); flex: none; }
  .brand__square { width: 24px; height: 24px; background: var(--brand-green); flex: none; }

  .page--back .lockup { left: 42px; bottom: 48px; }
  .page--front .lockup { left: 300px; top: 290px; }

  /* Contact panel */
  .contact {
    position: absolute; left: 300px; top: 395px;
    width: 165px; height: 190px;
    background: var(--brand-blue); color: var(--paper);
    padding: 20px 16px; font-size: 10.5px; line-height: 1.5; text-align: right;
  }
  .contact__title { font-weight: 700; font-size: 10.5px; letter-spacing: 0.3px; margin-bottom: 8px; text-align: left; }
  .contact__block { margin-bottom: 10px; }

  /* Front: image grid */
  .tile-grid {
    position: absolute; left: 290px; top: 28px;
    display: grid; grid-template-columns: 66px 66px; grid-template-rows: 66px 66px; gap: 8px;
  }
  .tile--green { background: var(--brand-green); }
  .tile--blue { background: var(--brand-blue); }
  .tile--forest { background: radial-gradient(circle at 60% 40%, #d8efb0 0%, #8cbf4a 35%, #3f7a2a 100%); }
  .tile--pylon { background: linear-gradient(180deg, #b9c7dc 0%, #6f86ad 55%, #3e5580 100%); }

  /* Front: message panels */
  .values {
    position: absolute; left: 80px; top: 150px;
    width: 185px; height: 170px;
    background: var(--brand-green); color: var(--paper);
    padding: 34px 16px 0 18px;
    font-size: 10px; font-weight: 300; line-height: 2;
  }
  .values li { list-style: none; }
  .headline {
    position: absolute; left: 80px; top: 320px;
    width: 185px; height: 190px;
    background: var(--brand-blue); color: var(--paper);
    padding: 72px 18px 0;
    text-align: center; font-weight: 300;
  }
  .headline__small { display: block; font-size: 15px; letter-spacing: 0.5px; }
  .headline__large { display: block; font-size: 30px; letter-spacing: 1px; line-height: 1.15; }
</style>
</head>
<body>
  <main class="spread">
    <section class="page page--back" aria-label="Back cover">
      <div class="lockup">
        <div class="brand"><span class="brand__dot"></span>Lakeshore Power</div>
        <div class="brand brand--efficiency"><span class="brand__square"></span>Verdant Efficiency Group</div>
      </div>
      <address class="contact" style="font-style: normal;">
        <p class="contact__title">ILLINOIS HEADQUARTERS</p>
        <p class="contact__block">742 West Harbor Avenue<br>Suite 210<br>Chicago, IL 60654</p>
        <p class="contact__block">800.555.0142</p>
        <p>www.lakeshorepower.com<br>www.verdantefficiency.com</p>
      </address>
    </section>

    <section class="page page--front" aria-label="Front cover">
      <div class="tile-grid">
        <div class="tile tile--green"></div>
        <div class="tile tile--forest" role="img" aria-label="Photo of sunlight through a green forest canopy"></div>
        <div class="tile tile--pylon" role="img" aria-label="Photo of an electricity pylon against a blue sky"></div>
        <div class="tile tile--blue"></div>
      </div>
      <ul class="values">
        <li>We manage pricing volatility.</li>
        <li>We mitigate risk.</li>
        <li>We secure the lowest cost.</li>
        <li>We lower energy usage.</li>
        <li>We reflect your energy values.</li>
      </ul>
      <h1 class="headline">
        <span class="headline__small">EVERYTHING</span>
        <span class="headline__large">ENERGY</span>
      </h1>
      <div class="lockup">
        <div class="brand"><span class="brand__dot"></span>Lakeshore Power</div>
        <div class="brand brand--efficiency"><span class="brand__square"></span>Verdant Efficiency Group</div>
      </div>
    </section>
  </main>
</body>
</html>
```